Brightwell Consulting Business Card Design

Business Card Design for Brightwell Consulting. Brightwell Consulting is a boutique consultancy based in Atlanta, GA., that specializes in marketing strategy, organization planning, and leadership development. We provide solutions for small businesses and startups as well as Summit 400 companies.

http://brightwellconsulting.example/

Target Market(s)

We provide solutions for small businesses and startups as well as Summit 400 companies.

Industry/Entity Type

Consulting

Contact Information for Business Card

Two sided business card with priority on contact information, logo, tag line (Inspiration to Dream More, Do More, Become More)

Colors

Designer to choose colors to be used in the design.

Requirements
Must have
• contact information, logo, tag line (Inspiration to Dream More, Do More, Become More)
• Simple no over communication.
Nice to have
• I would like to see different placements of logo and creative use of both sides of the card
Should not have
• Do not put too much information on the card.

```html
<!DOCTYPE html>
<html lang="en">
<head>
<meta charset="utf-8">
<title>Brightwell Consulting – Business Card</title>
<link rel="stylesheet" href="https://fonts.googleapis.com/css2?family=Work+Sans:wght@300;400;600&family=Exo+2:wght@400&display=swap">
<style>
  :root {
    --backdrop: #1c1c1c;
    --card: #151515;
    --ink: #ffffff;
    --ink-soft: #e6e6e6;
  }
  * { margin: 0; padding: 0; box-sizing: border-box; }
  html, body {
    width: 1200px; height: 900px; overflow: hidden;
    background: var(--backdrop);
    font-family: "Work Sans", sans-serif;
    color: var(--ink);
  }
  .stage {
    width: 1200px; height: 900px;
    display: flex; flex-direction: column;
    align-items: center; justify-content: center; gap: 24px;
  }
  .card {
    width: 700px; height: 400px;
    background: var(--card);
    position: relative;
    overflow: hidden;
    box-shadow: 0 10px 30px rgba(0,0,0,.5);
  }
  /* wordmark */
  .wordmark { display: flex; flex-direction: column; align-items: center; }
  .wordmark-name { font-weight: 600; letter-spacing: 1px; line-height: 1; }
  .wordmark-row { display: flex; align-items: center; gap: 12px; }
  .wordmark-square { background: var(--ink); display: block; }
  .wordmark-sub { font-weight: 300; text-transform: uppercase; }

  /* front */
  .card-front .wordmark { position: absolute; left: 0; right: 0; top: 100px; }
  .card-front .wordmark-square { width: 26px; height: 26px; }
  .card-front .wordmark-name { font-size: 64px; }
  .card-front .wordmark-sub { font-size: 30px; margin-top: 10px; letter-spacing: 6px; }
  .tagline {
    position: absolute; left: 0; right: 0; top: 248px;
    text-align: center; font-size: 15px; font-weight: 300;
    letter-spacing: 1px; color: var(--ink-soft);
  }
  .front-web {
    position: absolute; left: 0; right: 0; bottom: 58px;
    text-align: center; font-size: 17px; letter-spacing: 2.5px;
  }

  /* back */
  .card-back .wordmark { position: absolute; left: 30px; top: 138px; width: 260px; }
  .card-back .wordmark-square { width: 16px; height: 16px; }
  .card-back .wordmark-name { font-size: 40px; }
  .card-back .wordmark-sub { font-size: 19px; margin-top: 8px; letter-spacing: 4px; }
  .divider {
    position: absolute; left: 318px; top: 75px;
    width: 2px; height: 240px; background: var(--ink);
  }
  .details { position: absolute; left: 346px; top: 78px; width: 334px; }
  .person-name {
    font-family: "Exo 2", sans-serif; font-size: 24px;
    letter-spacing: 2px; text-transform: uppercase;
  }
  .person-role { font-size: 16px; color: var(--ink-soft); margin-top: 2px; }
  .address { font-size: 16px; line-height: 1.3; margin-top: 22px; letter-spacing: .4px; }
  .contacts { list-style: none; margin-top: 20px; font-size: 15px; letter-spacing: .2px; }
  .contacts li { display: flex; align-items: center; gap: 12px; line-height: 1.55; white-space: nowrap; }
  .contacts svg { width: 14px; height: 14px; flex: none; fill: var(--ink); }
</style>
</head>
<body>
<main class="stage">
  <section class="card card-front" aria-label="Card front">
    <div class="wordmark">
      <div class="wordmark-row">
        <span class="wordmark-square"></span>
        <span class="wordmark-name">Brightwell</span>
      </div>
      <span class="wordmark-sub">Consulting</span>
    </div>
    <p class="tagline">Inspiration to Dream More, Do More, Become More</p>
    <p class="front-web">www.brightwellconsulting.example</p>
  </section>

  <section class="card card-back" aria-label="Card back">
    <div class="wordmark">
      <div class="wordmark-row">
        <span class="wordmark-square"></span>
        <span class="wordmark-name">Brightwell</span>
      </div>
      <span class="wordmark-sub">Consulting</span>
    </div>
    <div class="divider"></div>
    <div class="details">
      <p class="person-name">Daniel Reyes</p>
      <p class="person-role">Managing Director</p>
      <p class="address">48 Larchmont Ave, Suite 2B,<br>Atlanta, GA</p>
      <ul class="contacts">
        <li>
          <svg viewBox="0 0 24 24" aria-hidden="true"><path d="M6.6 10.8a15 15 0 0 0 6.6 6.6l2.2-2.2c.3-.3.7-.4 1-.2 1.1.4 2.3.6 3.6.6.6 0 1 .4 1 1V20c0 .6-.4 1-1 1A17 17 0 0 1 3 4c0-.6.4-1 1-1h3.5c.6 0 1 .4 1 1 0 1.3.2 2.5.6 3.6.1.3 0 .7-.2 1z"/></svg>
          555-010-2468
        </li>
        <li>
          <svg viewBox="0 0 24 24" aria-hidden="true"><path d="M2 5h20v14H2z M3.5 6.5 12 13l8.5-6.5" fill="none" stroke="#fff" stroke-width="2"/></svg>
          daniel@brightwellconsulting.example
        </li>
        <li>
          <svg viewBox="0 0 24 24" aria-hidden="true"><g fill="none" stroke="#fff" stroke-width="1.8"><circle cx="12" cy="12" r="9.5"/><ellipse cx="12" cy="12" rx="4" ry="9.5"/><path d="M2.5 12h19M4 7h16M4 17h16"/></g></svg>
          www.brightwellconsulting.example
        </li>
      </ul>
    </div>
  </section>
</main>
</body>
</html>
```